Business card design for Plumbing and Gas fitting company

We need a business card design for our plumbing and gas fitting company using the company logo and director details. Design should be modern and eye-catching however kept reasonably simple. This design should be targeted at commercial businesses/work so professionalism is key.

Target Market(s)

Commercial/business

Industry/Entity Type

Plumbing

Contact Information for Business Card

Warwick Tane
Director
027 815 0937
warwick@harbourlinepipeworks.example
PO Box 8716
Kereru Bay 3179

Font styles to use
Sans Serif

Requirements
Must have
• Logo
• Modern
• Kept simple
Nice to have
• Colour scheme based around logo

```html
<!DOCTYPE html>
<html lang="en">
<head>
<meta charset="utf-8">
<title>Harbourline Pipeworks – Business Card</title>
<link rel="stylesheet" href="https://fonts.googleapis.com/css2?family=Jost:wght@400;500;600&display=swap">
<style>
  :root {
    --page: #ffffff;
    --navy: #0d1039;
    --edge: #2a2d45;
    --dot-teal: rgba(16, 92, 134, 0.55);
    --brand-blue: #1a7dcf;
    --accent-orange: #f08024;
    --text-light: #ffffff;
  }
  * { box-sizing: border-box; margin: 0; padding: 0; }
  html, body {
    width: 1200px; height: 1200px; overflow: hidden;
    background: var(--page);
    font-family: "Jost", "Futura", sans-serif;
  }
  .canvas { position: relative; width: 1200px; height: 1200px; }

  .card {
    position: absolute; left: 151px; width: 903px; height: 516px;
    background: var(--navy);
    border: 1.5px solid var(--edge);
    overflow: hidden;
  }
  .card--front { top: 58px; }
  .card--back  { top: 636px; }

  .halftone { position: absolute; pointer-events: none; }
  .halftone--top-right {
    right: -60px; top: -60px; width: 560px; height: 420px;
    background: radial-gradient(ellipse at 85% 15%, var(--dot-teal) 0%, rgba(16,92,134,0.25) 40%, transparent 70%);
  }
  .halftone--bottom-left {
    left: -60px; bottom: -60px; width: 460px; height: 380px;
    background: radial-gradient(ellipse at 15% 85%, var(--dot-teal) 0%, rgba(16,92,134,0.25) 40%, transparent 70%);
  }

  .wordmark {
    position: absolute; display: flex; align-items: center;
    color: var(--brand-blue); font-weight: 600; white-space: nowrap;
  }
  .wordmark__dot { border-radius: 50%; background: var(--accent-orange); flex: none; }
  .card--front .wordmark {
    left: 0; right: 0; top: 226px; justify-content: center;
    font-size: 46px; gap: 16px;
  }
  .card--front .wordmark__dot { width: 34px; height: 34px; }
  .card--back .wordmark { left: 64px; top: 80px; font-size: 29px; gap: 10px; }
  .card--back .wordmark__dot { width: 22px; height: 22px; }

  .contact { position: absolute; left: 374px; top: 226px; color: var(--text-light); }
  .contact__name {
    font-size: 29px; font-weight: 500; letter-spacing: 0.24em; line-height: 1;
  }
  .contact__role {
    margin-top: 13px; font-size: 23px; font-weight: 400; letter-spacing: 0.18em;
    color: var(--accent-orange); line-height: 1;
  }
  .contact__lines { margin-top: 37px; font-size: 26px; font-weight: 400; line-height: 1; }
  .contact__row { display: flex; align-items: center; gap: 12px; }
  .contact__row + .contact__row { margin-top: 12px; }
  .contact__icon { width: 20px; height: 20px; flex: none; fill: var(--text-light); }
  .contact__address { margin-top: 16px; line-height: 28px; letter-spacing: 0.02em; }
</style>
</head>
<body>
<main class="canvas">
  <section class="card card--front">
    <div class="halftone halftone--top-right" role="img" aria-label="Soft halftone dot pattern"></div>
    <div class="halftone halftone--bottom-left" role="img" aria-label="Soft halftone dot pattern"></div>
    <div class="wordmark"><span class="wordmark__dot"></span>Harbourline Pipeworks</div>
  </section>

  <section class="card card--back">
    <div class="halftone halftone--top-right" role="img" aria-label="Soft halftone dot pattern"></div>
    <div class="halftone halftone--bottom-left" role="img" aria-label="Soft halftone dot pattern"></div>
    <div class="wordmark"><span class="wordmark__dot"></span>Harbourline Pipeworks</div>

    <div class="contact">
      <p class="contact__name">WARWICK TANE</p>
      <p class="contact__role">DIRECTOR</p>
      <div class="contact__lines">
        <p class="contact__row">
          <svg class="contact__icon" viewBox="0 0 24 24" aria-hidden="true"><path d="M6.6 2.5l3 3.6-1.8 2.2c1 2.6 3.3 5 6 6.1l2.1-1.8 3.6 3-1.9 3.4C11 18.3 5.7 13 4.2 4.4z"/></svg>
          027 815 0937
        </p>
        <p class="contact__row">
          <svg class="contact__icon" viewBox="0 0 24 24" aria-hidden="true"><path d="M2 5h20v14H2z M3.5 6.5v.4l8.5 6.3 8.5-6.3v-.4z" fill-rule="evenodd"/></svg>
          warwick@harbourlinepipeworks.example
        </p>
        <p class="contact__address">PO Box 8716<br>Kereru Bay 3179</p>
      </div>
    </div>
  </section>
</main>
</body>
</html>
```